Breezeway Comfort business cards design

Need a business card design for a Heating and Air Conditioning business. I need these items included.
Business name: Breezeway Comfort
Owner: Marcus Tollefsen
License # 2874590
Phone number # 555-382-4071
Email: breezewaycomfortair@mailvista.example
Sales
Service
Installation
Maintenance

Heating and Air Conditioning

Requirements
Must have
• Company name , license number , phone number , email

```html
<!DOCTYPE html>
<html lang="en">
<head>
<meta charset="utf-8">
<title>Breezeway Comfort — Business Cards</title>
<link rel="stylesheet" href="https://fonts.googleapis.com/css2?family=Exo+2:wght@400;500;600&display=swap">
<style>
  :root {
    --bg: #2a2a2a;
    --card-blue: #0a3fb0;
    --card-blue-deep: #0838a0;
    --white: #ffffff;
    --orange: #f5802a;
    --red: #e8354a;
    --navy: #0b2f8a;
  }
  * { box-sizing: border-box; margin: 0; padding: 0; }
  html, body { width: 1200px; height: 1015px; overflow: hidden; }
  body {
    background: var(--bg);
    font-family: "Exo 2", sans-serif;
    position: relative;
  }
  .card {
    position: absolute;
    left: 300px;
    width: 600px;
    height: 343px;
    border-radius: 4px;
    overflow: hidden;
    box-shadow: 0 10px 30px rgba(0,0,0,.5);
  }
  /* back of card */
  .card-back { top: 100px; background: var(--card-blue); }
  .brand-block {
    position: absolute; left: 0; right: 0; top: 112px;
    text-align: center;
  }
  .brand-name {
    font-weight: 600; font-size: 44px; letter-spacing: 4px;
    text-transform: uppercase; color: var(--white); line-height: 1.1;
  }
  .brand-rule {
    display: flex; align-items: center; justify-content: center; gap: 14px;
    margin-top: 10px;
  }
  .brand-rule span { display: block; width: 60px; height: 2px; background: var(--orange); }
  .brand-rule i { display: block; width: 10px; height: 10px; border-radius: 50%; background: var(--orange); }
  .services {
    position: absolute; left: 0; right: 0; top: 240px;
    display: flex; justify-content: center; align-items: center; gap: 10px;
    color: var(--white); font-size: 17px; font-weight: 500; letter-spacing: .5px;
  }
  .services .sep { width: 7px; height: 7px; border-radius: 50%; background: var(--orange); }

  /* front of card */
  .card-front { top: 572px; background: var(--card-blue-deep); }
  .front-art { position: absolute; inset: 0; }
  .owner {
    position: absolute; left: 42px; top: 80px;
  }
  .owner-name {
    color: var(--white); font-size: 24px; font-weight: 500;
    letter-spacing: 1.5px; text-transform: uppercase; white-space: nowrap;
  }
  .owner-role {
    color: var(--orange); font-size: 14px; letter-spacing: 1px; text-transform: uppercase;
  }
  .contact {
    position: absolute; left: 42px; top: 214px;
    color: var(--white); font-size: 14px; letter-spacing: .3px;
  }
  .license { margin-bottom: 18px; }
  .license .label { color: var(--orange); }
  .contact-line { display: flex; align-items: center; gap: 8px; margin-top: 6px; white-space: nowrap; }
  .contact-line svg { width: 14px; height: 14px; flex: none; }
  .front-brand {
    position: absolute; left: 385px; width: 200px; top: 98px;
    text-align: center;
  }
  .front-brand .brand-name { color: var(--navy); font-size: 26px; letter-spacing: 2px; }
  .front-brand .brand-rule span { width: 30px; }
</style>
</head>
<body>

<section class="card card-back" aria-label="Card back">
  <div class="brand-block">
    <div class="brand-name">Breezeway<br>Comfort</div>
    <div class="brand-rule"><span></span><i></i><span></span></div>
  </div>
  <div class="services">
    <span>Sales</span><i class="sep"></i>
    <span>Service</span><i class="sep"></i>
    <span>Installation</span><i class="sep"></i>
    <span>Maintenance</span>
  </div>
</section>

<section class="card card-front" aria-label="Card front">
  <svg class="front-art" viewBox="0 0 600 343" width="600" height="343" aria-hidden="true">
    <defs>
      <linearGradient id="arcGrad" x1="0" y1="0" x2="1" y2="1">
        <stop offset="0" stop-color="#f5802a"/>
        <stop offset="1" stop-color="#e8354a"/>
      </linearGradient>
    </defs>
    <circle cx="482" cy="140" r="172" fill="url(#arcGrad)"/>
    <circle cx="490" cy="134" r="168" fill="#ffffff"/>
  </svg>

  <div class="owner">
    <div class="owner-name">Marcus Tollefsen</div>
    <div class="owner-role">Owner</div>
  </div>

  <div class="contact">
    <div class="license"><span class="label">License</span> # 2874590</div>
    <div class="contact-line">
      <svg viewBox="0 0 24 24"><path fill="#f5802a" d="M6.6 10.8a15 15 0 0 0 6.6 6.6l2.2-2.2a1 1 0 0 1 1-.25 11.4 11.4 0 0 0 3.6.57 1 1 0 0 1 1 1V20a1 1 0 0 1-1 1A17 17 0 0 1 3 4a1 1 0 0 1 1-1h3.5a1 1 0 0 1 1 1c0 1.25.2 2.45.57 3.6a1 1 0 0 1-.25 1z"/></svg>
      <span>555-382-4071</span>
    </div>
    <div class="contact-line">
      <svg viewBox="0 0 24 24"><path fill="#f5802a" d="M2 5h20v14H2z"/><path fill="none" stroke="#0838a0" stroke-width="1.6" d="M2 5l10 8 10-8"/></svg>
      <span>breezewaycomfortair@mailvista.example</span>
    </div>
  </div>

  <div class="front-brand">
    <div class="brand-name">Breezeway<br>Comfort</div>
    <div class="brand-rule"><span></span><i></i><span></span></div>
  </div>
</section>

</body>
</html>
```